TALVERN CREST LIMITED CALENDAR 2018

We need an innovative calendar design for our company for 2018. to give a brief description of our company:
"Talvern Crest was founded in 2016 to provide a wide range of management consultancy and advisory services to small and medium-sized companies operating in consumer-driven sectors. With more than 300 years of cumulative investment and advisory experience among our sector-focused seasoned professionals, we advise management teams on an aggregate of $850m worth of investments operating in the healthcare, education, food and beverage and logistics sectors within the MENASEA region; the region of our expertise."
We want the design to include the following 12 countries for each month:
1. UAE 2. Saudi Arabia 3. Kuwait 4. Bahrain 5. Qatar 6. Oman 7. Jordan 8. Egypt 9. Singapore 10. Malaysia 11. Thailand 12. Indonesia
The description/design for each month must include each country's economic growth, Per Capita Income, GDP, etc. That is what we wish for the final design for each month to communicate as our company is in to a wide range of Investment management and Advisory Services
Target Market(s)
FINANCIAL SERVICES AND CONSULTING
Industry/Entity Type
Financial Service
Font styles to use
Colors
Designer to choose colors to be used in the design.
Look and feel

```html
<!DOCTYPE html>
<html lang="en">
<head>
<meta charset="utf-8">
<title>Talvern Crest Calendar 2018 – December</title>
<link rel="stylesheet" href="https://fonts.googleapis.com/css2?family=Great+Vibes&family=Open+Sans:ital,wght@0,400;0,600;0,700;1,400;1,600;1,700&family=Montserrat:wght@700;800&display=swap">
<style>
  :root{
    --navy:#1d2a44;
    --navy-deep:#141d33;
    --gold:#b8892b;
    --gold-light:#d3a84a;
    --maroon:#8a1c2c;
    --cell:#ededed;
    --cell-dark:#d9d9d9;
    --ink:#222;
    --white:#fff;
    --sky-top:#3f7fc2;
    --sky-mid:#9cc3e4;
    --city:#b9a98f;
  }
  *{margin:0;padding:0;box-sizing:border-box}
  html,body{width:1200px;height:847px;overflow:hidden;background:var(--white)}
  .calendar-page{position:relative;width:1200px;height:847px;overflow:hidden;background:var(--white);font-family:"Open Sans",Arial,sans-serif;color:var(--ink)}
  .backdrop{position:absolute;inset:0}
  .month-head{position:absolute;left:672px;top:62px;display:flex;align-items:flex-end}
  .year{font-family:"Montserrat",Arial,sans-serif;font-weight:800;font-size:46px;color:var(--gold);line-height:1;padding-bottom:8px;width:214px;border-bottom:3px solid var(--gold)}
  .month{font-family:"Great Vibes",cursive;font-size:70px;color:var(--maroon);line-height:1;margin-left:10px;margin-bottom:-6px;white-space:nowrap}
  .month-grid{position:absolute;left:666px;top:182px;width:508px;border-collapse:separate;border-spacing:3px;table-layout:fixed}
  .month-grid th{background:var(--cell);color:var(--maroon);font-weight:700;font-size:15px;text-align:left;padding:2px 6px;height:22px}
  .month-grid td{background:var(--cell);font-weight:600;font-size:17px;text-align:left;vertical-align:top;padding:6px 6px;height:56px}
  .month-grid .sat{background:var(--cell-dark)}
  .brand{position:absolute;left:670px;top:508px;width:236px;height:58px;border:2px solid var(--gold);display:flex;align-items:center;justify-content:center;font-family:"Open Sans",Arial,sans-serif;font-weight:700;font-size:21px;letter-spacing:1.5px;white-space:nowrap;color:var(--gold);background:var(--white)}
  .about{position:absolute;left:686px;top:578px;width:486px;font-size:12.5px;line-height:1.3;color:var(--ink)}
  .about strong{font-style:italic;font-weight:700}
  .tagline{position:absolute;left:712px;top:638px;font-style:italic;font-weight:600;font-size:16px;color:var(--ink);white-space:nowrap}
  .web-pill{position:absolute;left:896px;top:664px;width:304px;height:34px;background:var(--gold);border-radius:17px 0 0 17px;color:var(--white);font-weight:700;font-size:17px;display:flex;align-items:center;padding-left:36px;white-space:nowrap}
  .stats-bar{position:absolute;left:0;top:721px;width:1200px;height:126px;background:var(--navy-deep);color:var(--white)}
  .country{position:absolute;left:132px;top:8px;font-family:"Montserrat",Arial,sans-serif;font-weight:800;font-size:44px;color:var(--gold-light)}
  .pin{position:absolute;left:92px;top:14px}
  .growth-label{position:absolute;left:130px;top:68px;font-size:17px;color:var(--white);white-space:nowrap}
  .stats-year{position:absolute;left:430px;top:4px;width:760px;text-align:center;font-family:"Montserrat",Arial,sans-serif;font-weight:800;font-size:28px;border-bottom:2px solid var(--white);padding-bottom:2px}
  .stat{position:absolute;top:50px;white-space:nowrap}
  .stat-label{font-style:italic;font-weight:700;font-size:18px}
  .stat-value{font-weight:700;font-size:22px;margin-top:6px}
  .stat-pop{left:432px}
  .stat-gdp{left:735px}
  .stat-gdp .stat-label{padding-left:36px}
  .stat-income{left:975px}
</style>
</head>
<body>
<main class="calendar-page">
  <svg class="backdrop" width="1200" height="847" viewBox="0 0 1200 847">
    <defs>
      <linearGradient id="skylineTones" x1="0" y1="0" x2="0" y2="1">
        <stop offset="0" stop-color="var(--sky-top)"/>
        <stop offset="0.5" stop-color="var(--sky-mid)"/>
        <stop offset="0.7" stop-color="var(--city)"/>
        <stop offset="1" stop-color="#5f6f78"/>
      </linearGradient>
    </defs>
    <polygon points="0,0 392,0 572,721 0,721" fill="url(#skylineTones)" role="img" aria-label="Photograph of a supertall tower rising over the Dubai city skyline and coastline"/>
    <polygon points="392,0 440,0 618,721 572,721" fill="var(--navy)"/>
    <polygon points="560,470 600,470 680,721 618,721" fill="var(--gold)"/>
    <polygon points="1150,721 1200,600 1200,721" fill="var(--gold)"/>
  </svg>

  <header class="month-head">
    <span class="year">2018</span>
    <span class="month">December</span>
  </header>

  <table class="month-grid">
    <thead>
      <tr><th>Sun</th><th>Mon</th><th>Tue</th><th>Wed</th><th>Thu</th><th>Fri</th><th class="sat">Sat</th></tr>
    </thead>
    <tbody>
      <tr><td>30</td><td>31</td><td></td><td></td><td></td><td></td><td class="sat">1</td></tr>
      <tr><td>2</td><td>3</td><td>4</td><td>5</td><td>6</td><td>7</td><td class="sat">8</td></tr>
      <tr><td>9</td><td>10</td><td>11</td><td>12</td><td>13</td><td>14</td><td class="sat">15</td></tr>
      <tr><td>16</td><td>17</td><td>18</td><td>19</td><td>20</td><td>21</td><td class="sat">22</td></tr>
      <tr><td>23</td><td>24</td><td>25</td><td>26</td><td>27</td><td>28</td><td class="sat">29</td></tr>
    </tbody>
  </table>

  <div class="brand">TALVERN CREST</div>
  <p class="about"><strong>Talvern Crest</strong> was founded in 2016 to provide a wide range of management consultancy and advisory services to small and medium-sized companies operating in consumer-driven sectors.</p>
  <p class="tagline">"Working with you towards building a better business..."</p>
  <div class="web-pill">www.talvern-crest.com</div>

  <section class="stats-bar">
    <svg class="pin" width="34" height="46" viewBox="0 0 34 46" aria-hidden="true">
      <path d="M17 2C9 2 3 8 3 16c0 11 14 27 14 27s14-16 14-27C31 8 25 2 17 2z" fill="none" stroke="var(--gold-light)" stroke-width="4"/>
      <circle cx="17" cy="16" r="5" fill="var(--gold-light)"/>
    </svg>
    <div class="country">UAE</div>
    <div class="growth-label">Country's Economic Growth:</div>
    <div class="stats-year">2017</div>
    <div class="stat stat-pop"><div class="stat-label">Population</div><div class="stat-value">9.40 million</div></div>
    <div class="stat stat-gdp"><div class="stat-label">GDP</div><div class="stat-value">USD 407.6 billion</div></div>
    <div class="stat stat-income"><div class="stat-label">Per Capita Income</div><div class="stat-value">USD 40,197.9</div></div>
  </section>
</main>
</body>
</html>
```